Awesome business card design needed

We need a new business card design to go with our new logo.
We are a web development agency that specialises in highly complex back-end integrations as opposed to design, our customers are retailers, hotels, hospitals and any other organisation that has a large online marketing department.
Take a look at our website - www.orvekplus.com for some inspiration.
We want our new business cards to exude class, professionalism and style.
We are likely to choose a high-end card to print them on but we want the design of the card itself to really turn heads.
We have no specific colour requirements, the logo as you will see is a turquoise colour R89 G171 B167 #59aba7 but it can also be in white if you want to make the colour of the card something different.
The information on the card should be:
Name
Position
Tel
email
Potentially a double sided card could have our web address, twitter and FB links.

```html
<!DOCTYPE html>
<html lang="en">
<head>
<meta charset="utf-8">
<title>orvekplus business card</title>
<link rel="stylesheet" href="https://fonts.googleapis.com/css2?family=Arimo:wght@400;700&display=swap">
<style>
  :root {
    --page: #ffffff;
    --shadow: #e6e6e6;
    --front: #54d9a0;
    --mint: #a8f7da;
    --back: #000000;
    --white: #ffffff;
    --square: #2f8f6a;
  }
  html, body {
    margin: 0;
    padding: 0;
    overflow: hidden;
    background: var(--page);
  }
  .canvas {
    position: relative;
    width: 1200px;
    height: 349px;
    overflow: hidden;
    background: var(--page);
    font-family: "Arimo", Arial, sans-serif;
  }
  .card-shadow {
    position: absolute;
    background: var(--shadow);
  }
  .card-shadow--front { left: 40px; top: 22px; width: 555px; height: 318px; }
  .card-shadow--back { left: 615px; top: 25px; width: 560px; height: 320px; }

  .card {
    position: absolute;
    box-sizing: border-box;
    overflow: hidden;
  }
  .card--front {
    left: 25px; top: 5px; width: 558px; height: 316px;
    background: var(--front);
    border: 1px solid #333;
  }
  .card--back {
    left: 640px; top: 5px; width: 548px; height: 317px;
    background: var(--back);
  }

  .stacked-name {
    position: absolute;
    left: 8px; top: 0;
    margin: 0;
    color: var(--mint);
    font-weight: 700;
    font-size: 88px;
    line-height: 103px;
    letter-spacing: 4px;
  }
  .card--back .stacked-name { left: 12px; top: 2px; }

  .front-name {
    position: absolute;
    left: 230px; top: 88px;
    margin: 0;
    color: var(--white);
    font-weight: 700;
    font-size: 60px;
    letter-spacing: 2px;
  }

  .links {
    position: absolute;
    left: 300px; top: 218px;
    margin: 0; padding: 0;
    list-style: none;
  }
  .links li {
    display: flex;
    align-items: center;
    height: 38px;
  }
  .links .square {
    width: 34px; height: 34px;
    background: var(--square);
    margin-right: 20px;
  }
  .links span {
    color: var(--white);
    font-size: 14px;
    letter-spacing: 0.8px;
  }

  .back-name {
    position: absolute;
    right: 18px; top: 18px;
    margin: 0;
    color: var(--mint);
    font-weight: 700;
    font-size: 52px;
    letter-spacing: 1px;
  }
  .person {
    position: absolute;
    right: 18px; top: 134px;
    text-align: right;
    color: var(--white);
    font-weight: 700;
  }
  .person__name { margin: 0; font-size: 25px; line-height: 30px; }
  .person__role { margin: 2px 0 0; font-size: 14px; letter-spacing: 0.5px; }
  .contact {
    position: absolute;
    right: 18px; top: 225px;
    margin: 0; padding: 0;
    list-style: none;
    text-align: right;
    color: var(--white);
    font-weight: 700;
    font-size: 15px;
    line-height: 19.5px;
    letter-spacing: 0.5px;
  }
</style>
</head>
<body>
  <div class="canvas">
    <div class="card-shadow card-shadow--front"></div>
    <div class="card-shadow card-shadow--back"></div>

    <section class="card card--front" aria-label="Card front">
      <p class="stacked-name">orv<br>ek<br>plus</p>
      <h1 class="front-name">orvekplus</h1>
      <ul class="links">
        <li><div class="square"></div><span>https://www.friendwall.com/</span></li>
        <li><div class="square"></div><span>https://chirpline.com/login</span></li>
      </ul>
    </section>

    <section class="card card--back" aria-label="Card back">
      <p class="stacked-name">orv<br>ek<br>plus</p>
      <h2 class="back-name">orvekplus</h2>
      <div class="person">
        <p class="person__name">Mara Velden</p>
        <p class="person__role">MANAGER</p>
      </div>
      <ul class="contact">
        <li>Phone Number</li>
        <li>E-mail</li>
        <li>Wed b Address</li>
      </ul>
    </section>
  </div>
</body>
</html>
```